Asphalt Driveway Billboard Design

We need a billboard designed for an Asphalt & Concrete Company in Minnesota. We want to advertise Asphalt Driveways on this billboard! Logo is uploaded below. Our website is pinecrest-paving.net for more information.

```html
<!DOCTYPE html>
<html lang="en">
<head>
<meta charset="UTF-8">
<title>Pinecrest Paving – Asphalt Driveway Billboard</title>
<link rel="stylesheet" href="https://fonts.googleapis.com/css2?family=Montserrat:wght@500;600;700;800&display=swap">
<style>
  :root {
    --brand-blue: #0f5aa6;
    --bright-blue: #1d74c9;
    --sky-blue: #3fb4ee;
    --ink: #161616;
    --photo-top: #6f98bd;
    --photo-bottom: #44474b;
    --white: #ffffff;
    --page: #b9b9b9;
  }
  * { margin: 0; padding: 0; box-sizing: border-box; }
  html, body {
    width: 980px; height: 1200px; overflow: hidden;
    background: radial-gradient(circle at 50% 45%, #d3d3d3, var(--page));
    font-family: "Montserrat", sans-serif;
  }
  .billboard-frame {
    position: absolute; left: 30px; top: 384px;
    width: 920px; height: 432px;
    box-shadow: 0 10px 30px rgba(0,0,0,0.25);
    overflow: hidden;
  }
  .billboard {
    position: absolute; left: 0; top: 0;
    width: 1521px; height: 715px;
    transform: scale(0.6049); transform-origin: 0 0;
    background: var(--brand-blue);
    color: var(--white);
  }
  .house-photo {
    position: absolute; inset: 0;
    clip-path: polygon(905px 0, 1521px 0, 1521px 715px, 650px 715px);
    background: linear-gradient(180deg, var(--photo-top), var(--photo-bottom));
  }
  .shapes { position: absolute; inset: 0; }
  .headline {
    position: absolute; left: 44px; top: 36px;
    font-weight: 800; font-size: 66px; line-height: 66px;
    letter-spacing: 2px;
  }
  .tagline {
    position: absolute; left: 46px; top: 212px;
    font-weight: 700; font-size: 25px; letter-spacing: 1.6px;
  }
  .sub-tagline {
    position: absolute; left: 46px; top: 262px;
    font-weight: 600; font-size: 25px; letter-spacing: 1.2px;
  }
  .tab-label {
    position: absolute; left: 68px;
    font-weight: 800; font-size: 27px; letter-spacing: 1.6px;
    color: var(--brand-blue);
  }
  .tab-label.provide { top: 335px; }
  .tab-label.estimate { top: 563px; }
  .service {
    position: absolute; display: flex; align-items: center; gap: 14px;
    font-weight: 600; font-size: 19px; line-height: 21px; letter-spacing: 1px;
  }
  .service-icon {
    width: 44px; height: 44px; background: var(--ink);
    display: flex; align-items: center; justify-content: center; flex: none;
  }
  .contact {
    position: absolute; top: 627px; display: flex; align-items: center; gap: 14px;
  }
  .contact-icon {
    width: 44px; height: 44px; background: var(--bright-blue);
    display: flex; align-items: center; justify-content: center;
  }
  .phone-number { font-weight: 800; font-size: 38px; letter-spacing: 1.5px; }
  .web-address { font-weight: 500; font-size: 25px; letter-spacing: 1.5px; }
  .web-address strong { font-weight: 700; }
  .brand-name {
    position: absolute; left: 1230px; top: 560px; width: 260px;
    text-align: center; color: var(--ink);
    font-weight: 800; font-size: 34px; line-height: 38px; letter-spacing: 1px;
  }
</style>
</head>
<body>
  <div class="billboard-frame">
    <div class="billboard">
      <div class="house-photo" role="img" aria-label="Photo of a two-storey house with a double garage and a freshly paved black asphalt driveway"></div>

      <svg class="shapes" viewBox="0 0 1521 715" width="1521" height="715">
        <g fill="#2f8fd8" opacity="0.55">
          <polygon points="880,0 905,0 650,715 620,715"/>
        </g>
        <g fill="var(--sky-blue)">
          <polygon points="880,0 918,0 914,10 876,10"/>
          <polygon points="868,32 906,32 899,52 861,52"/>
          <polygon points="853,74 891,74 884,94 846,94"/>
          <polygon points="838,116 876,116 869,136 831,136"/>
          <polygon points="823,158 861,158 854,178 816,178"/>
          <polygon points="808,200 846,200 839,220 801,220" opacity="0.85"/>
          <polygon points="793,242 831,242 824,262 786,262" opacity="0.8"/>
          <polygon points="778,284 816,284 809,304 771,304" opacity="0.7"/>
          <polygon points="763,326 801,326 794,346 756,346" opacity="0.6"/>
          <polygon points="748,368 786,368 779,388 741,388" opacity="0.5"/>
          <polygon points="733,410 771,410 764,430 726,430" opacity="0.4"/>
          <polygon points="718,452 756,452 749,472 711,472" opacity="0.3"/>
          <polygon points="703,494 741,494 734,514 696,514" opacity="0.2"/>
        </g>
        <polygon points="0,201 742,201 720,255 0,255" fill="var(--ink)"/>
        <polygon points="44,330 294,330 310,375 44,375" fill="var(--white)"/>
        <rect x="300" y="371" width="362" height="4" fill="var(--white)"/>
        <polygon points="0,580 843,580 903,715 0,715" fill="var(--ink)"/>
        <polygon points="44,558 334,558 350,603 44,603" fill="var(--white)"/>
        <polygon points="1288,455 1521,455 1521,715 1168,715" fill="var(--white)"/>
      </svg>

      <h1 class="headline">ASPHALT DRIVEWAY<br>REPLACEMENT</h1>
      <p class="tagline">YOU DESERVE TO COME HOME TO QUALITY</p>
      <p class="sub-tagline">We’re here to help you smooth things over.</p>

      <p class="tab-label provide">WE PROVIDE</p>

      <div class="service" style="left:44px; top:398px;">
        <span class="service-icon">
          <svg width="28" height="28" viewBox="0 0 28 28" fill="none" stroke="#fff" stroke-width="1.6"><circle cx="14" cy="10" r="4"/><path d="M6 24c0-5 4-8 8-8s8 3 8 8"/><path d="M14 2l1 2h2l-1.5 1.3.5 2-2-1.2-2 1.2.5-2L11 4h2z"/></svg>
        </span>
        <span>Asphalt Driveway<br>Specialists</span>
      </div>
      <div class="service" style="left:330px; top:398px;">
        <span class="service-icon">
          <svg width="28" height="28" viewBox="0 0 28 28" fill="none" stroke="#fff" stroke-width="1.6"><path d="M14 3l9 4v6c0 6-4 10-9 12-5-2-9-6-9-12V7z"/><path d="M9.5 14l3 3 6-6"/></svg>
        </span>
        <span>Asphalt Driveway<br>Replacement Warranty</span>
      </div>
      <div class="service" style="left:44px; top:455px;">
        <span class="service-icon">
          <svg width="28" height="28" viewBox="0 0 28 28" fill="none" stroke="#fff" stroke-width="1.6"><path d="M7 12a7 7 0 0 1 14 0"/><path d="M5 12h18"/><path d="M6 25c0-5 4-8 8-8s8 3 8 8"/><path d="M17 22l2 2 4-4"/></svg>
        </span>
        <span>Asphalt Driveway<br>Replacement And Experienced Professionals</span>
      </div>

      <p class="tab-label estimate">FREE ESTIMATE</p>

      <div class="contact" style="left:44px;">
        <span class="contact-icon">
          <svg width="26" height="26" viewBox="0 0 24 24" fill="none" stroke="#fff" stroke-width="1.6" stroke-linejoin="round"><path d="M5 3h4l2 5-2.5 1.5a11 11 0 0 0 6 6L16 13l5 2v4a2 2 0 0 1-2 2A16 16 0 0 1 3 5a2 2 0 0 1 2-2z"/></svg>
        </span>
        <span class="phone-number">763-555-0148</span>
      </div>
      <div class="contact" style="left:417px;">
        <span class="contact-icon">
          <svg width="28" height="28" viewBox="0 0 24 24" fill="none" stroke="#fff" stroke-width="1.5"><circle cx="12" cy="12" r="9"/><ellipse cx="12" cy="12" rx="4" ry="9"/><path d="M3 12h18M4.5 7.5h15M4.5 16.5h15"/></svg>
        </span>
        <span class="web-address">www.<strong>pinecrest-paving</strong>.net</span>
      </div>

      <p class="brand-name">PINECREST<br>PAVING</p>
    </div>
  </div>
</body>
</html>
```